Electrical company business card design.

Hi, were an electrical company in Tarnview New Zealand called Quarneth Ltd. We focus mainly on high end residential and commercial so the card would be targeted towards that.
The card will be for myself, i am the director of the company.
Name: Derek Olstow
Position: Director/electrician
Phone: 021 387 9415
Email: derek@quarneth.co.nz
Location: Tarnview
As for colors the the blue color in the logo is preferred, i also don't mind a black background option.
Target Market(s)
High end residential and commercial
Industry/Entity Type
Electrician
Contact Information for Business Card
Name: Derek Olstow Position: Director/Electrician Phone: 021 387 9415, Email: derek@quarneth.co.nz, Location: Tarnview

```html
<!DOCTYPE html>
<html lang="en">
<head>
<meta charset="utf-8">
<title>Quarneth Ltd – Business Card</title>
<link href="https://fonts.googleapis.com/css2?family=Montserrat:wght@700&family=Lato:wght@400&display=swap" rel="stylesheet">
<style>
  :root {
    --backdrop: #a0a0a0;
    --card: #ffffff;
    --brand-blue: #1a4aa0;
    --bar-light: #29a6e0;
    --bar-dark: #1a46a0;
    --ink-grey: #55585b;
    --text-grey: #4a4a4a;
    --white: #ffffff;
  }
  * { margin: 0; padding: 0; box-sizing: border-box; }
  html, body {
    width: 1200px;
    height: 1200px;
    overflow: hidden;
    background: var(--backdrop);
  }
  .canvas {
    position: relative;
    width: 1200px;
    height: 1200px;
  }
  .card {
    position: absolute;
    left: 161px;
    width: 877px;
    height: 514px;
    background: var(--card);
    overflow: hidden;
  }
  .card--front { top: 68px; }
  .card--back { top: 620px; }

  .holder-name {
    position: absolute;
    left: 88px;
    top: 86px;
    font-family: "Montserrat", sans-serif;
    font-weight: 700;
    font-size: 35px;
    line-height: 45px;
    letter-spacing: 1px;
    color: var(--brand-blue);
    text-transform: uppercase;
  }
  .holder-role {
    position: absolute;
    left: 88px;
    top: 180px;
    font-family: "Lato", sans-serif;
    font-size: 19px;
    color: var(--text-grey);
  }

  .contact-bar {
    position: absolute;
    left: 49px;
    width: 313px;
    height: 65px;
    background: linear-gradient(90deg, var(--bar-light), var(--bar-dark));
    display: flex;
    align-items: center;
    padding-left: 38px;
    font-family: "Lato", sans-serif;
    font-size: 28px;
    color: var(--white);
  }
  .contact-bar svg { width: 26px; height: 34px; margin-right: 22px; flex: none; }
  .contact-bar--phone { top: 287px; }
  .contact-bar--location { top: 362px; }

  .edge-tab {
    position: absolute;
    right: 0;
    width: 31px;
    height: 65px;
    background: linear-gradient(90deg, var(--bar-light), var(--bar-dark));
  }
  .edge-tab--upper { top: 287px; }
  .edge-tab--lower { top: 362px; }

  .front-brand {
    position: absolute;
    left: 411px;
    top: 87px;
    width: 386px;
    height: 339px;
    display: flex;
    align-items: center;
    justify-content: center;
    font-family: "Montserrat", sans-serif;
    font-weight: 700;
    font-size: 62px;
    color: var(--brand-blue);
  }

  .back-brand {
    position: absolute;
    inset: 0;
    display: flex;
    align-items: center;
    justify-content: center;
    gap: 24px;
  }
  .back-brand__square {
    width: 56px;
    height: 56px;
    background: linear-gradient(135deg, var(--bar-light), var(--bar-dark));
  }
  .back-brand__name {
    font-family: "Montserrat", sans-serif;
    font-weight: 700;
    font-size: 72px;
    letter-spacing: 3px;
    color: var(--ink-grey);
    text-transform: uppercase;
  }
</style>
</head>
<body>
<div class="canvas">

  <section class="card card--front">
    <h1 class="holder-name">Derek<br>Olstow</h1>
    <p class="holder-role">Director/electrician</p>

    <div class="contact-bar contact-bar--phone">
      <svg viewBox="0 0 26 34" aria-hidden="true">
        <rect x="3" y="1" width="20" height="32" rx="3" fill="none" stroke="#fff" stroke-width="2.5"/>
        <line x1="3" y1="6" x2="23" y2="6" stroke="#fff" stroke-width="2"/>
        <line x1="3" y1="27" x2="23" y2="27" stroke="#fff" stroke-width="2"/>
        <circle cx="13" cy="30" r="1.4" fill="#fff"/>
      </svg>
      <span>021 387 9415</span>
    </div>

    <div class="contact-bar contact-bar--location">
      <svg viewBox="0 0 26 34" aria-hidden="true">
        <path d="M13 1C6.4 1 1 6.2 1 12.7 1 21 13 33 13 33s12-12 12-20.3C25 6.2 19.6 1 13 1z" fill="#fff"/>
        <circle cx="13" cy="12.5" r="4.5" fill="#2a7ccc"/>
      </svg>
      <span>Tarnview</span>
    </div>

    <div class="edge-tab edge-tab--upper"></div>
    <div class="edge-tab edge-tab--lower"></div>

    <div class="front-brand">Quarneth</div>
  </section>

  <section class="card card--back">
    <div class="back-brand">
      <span class="back-brand__square"></span>
      <span class="back-brand__name">Quarneth</span>
    </div>
  </section>

</div>
</body>
</html>
```